PELDIVUX HOA Portal Site for Public

Clean up and organize current website; need website to look good and functional; this is a HOA (homeowner association management) website where homeowners can login and pay their bill, general information about a HOA, monthly newsletter page.
Competitors:
https://lumaridge.example/
https://bexolirnada.example/
https://www.qvhabitations.example/nevada
http://www.tpq-hoa.example/

Target Market(s)

homeowners

Industry/Entity Type

Real Estate

Coding

Coded - Design and coding required

Number of Pages Required

5+ page

Font styles to use
Serif

Colors
0292cd
33a6d7
e667a6
e34297

Requirements
Must have
• login to pay
• services page
• contact us
• order resale package
Nice to have
• page why an HOA would contract us

```html
<!DOCTYPE html>
<html lang="en">
<head>
<meta charset="utf-8">
<title>PELDIVUX – HOA Management</title>
<link href="https://fonts.googleapis.com/css2?family=Mulish:wght@300;400;600;700&display=swap" rel="stylesheet">
<style>
:root{
  --blue:#0292cd;
  --blue-light:#33a6d7;
  --pink:#e667a6;
  --pink-deep:#e34297;
  --ink:#222;
  --text:#777;
  --line:#e6e6e6;
  --soft:#f7f7f7;
  --dark:#262222;
  --white:#fff;
}
*{box-sizing:border-box;margin:0;padding:0}
html,body{width:1200px;height:4751px;overflow:hidden}
body{position:relative;font-family:"Mulish",sans-serif;color:var(--ink);background:var(--white)}
section,header,footer{position:absolute;left:0;width:1200px}
.abs{position:absolute}

/* header */
.site-header{top:0;height:65px;border-top:4px solid var(--blue);background:var(--white);border-bottom:1px solid var(--line)}
.brand{left:92px;top:22px;font-weight:700;font-size:14px;color:var(--ink)}
.nav-item{top:22px;font-size:12px;color:#444}
.nav-item.active{top:0;left:264px;width:71px;height:61px;background:var(--blue);color:var(--white);display:flex;align-items:center;justify-content:center}
.phone-dot{left:926px;top:19px;width:24px;height:24px;border-radius:50%;background:var(--blue);display:flex;align-items:center;justify-content:center}
.phone-num{left:958px;top:23px;font-size:12px;color:#444}

/* hero */
.hero{top:65px;height:567px;background:linear-gradient(110deg,#5b6a4e 0%,#8e9680 25%,#c9ccc6 50%,#d9d4cd 72%,#b7aba0 100%)}
.hero h1{left:92px;top:155px;width:520px;font-size:37px;line-height:46px;font-weight:700;color:var(--white)}
.hero p{left:92px;top:308px;width:520px;font-size:13px;line-height:20px;color:var(--white)}
.btn-outline{left:92px;top:383px;width:133px;height:44px;border:2px solid var(--white);border-radius:22px;color:var(--white);font-size:12px;display:flex;align-items:center;justify-content:center}

/* services */
.services{top:720px;height:350px}
.service-card{top:0;width:317px;border:1px solid var(--line);padding:63px 37px 0}
.service-num{width:52px;height:52px;border-radius:50%;background:var(--pink-deep);color:var(--white);font-size:21px;display:flex;align-items:center;justify-content:center}
.service-card h3{margin-top:27px;font-size:17px;font-weight:600;letter-spacing:.3px}
.service-card p{margin-top:12px;font-size:11.5px;line-height:21px;color:var(--text)}

/* duties */
.duties{top:1240px;height:440px}
.duties h2{left:92px;top:14px;width:500px;font-size:25px;line-height:35px;font-weight:600}
.duty{left:110px;width:460px}
.duty-icon{left:0;top:4px;width:45px;height:45px;border-radius:50%;background:var(--blue);display:flex;align-items:center;justify-content:center}
.duty h4{position:absolute;left:62px;top:0;font-size:18px;font-weight:600}
.duty p{position:absolute;left:62px;top:26px;width:380px;font-size:11px;line-height:21px;color:var(--text)}
.signup{left:693px;top:-3px;width:394px;height:394px;border-radius:50%;background:var(--dark)}
.signup h3{position:absolute;left:0;width:394px;top:75px;text-align:center;color:var(--white);font-size:24px;font-weight:600}
.field{position:absolute;left:82px;width:232px;height:34px;border-bottom:1px solid #555;color:#aaa;font-size:11px;padding-top:12px;padding-left:2px}
.signup .btn-white{position:absolute;left:136px;top:291px;width:123px;height:42px;border-radius:21px;background:var(--white);color:var(--ink);font-size:11px;display:flex;align-items:center;justify-content:center}

/* team */
.team{top:1749px;height:643px;background:var(--soft)}
.section-title{position:absolute;left:0;width:1200px;text-align:center;font-size:26px;font-weight:600}
.section-sub{position:absolute;left:0;width:1200px;text-align:center;font-size:14px;color:var(--text)}
.member{top:184px;width:229px;height:371px;background:var(--white)}
.member-photo{height:244px;background:linear-gradient(180deg,#eeeeee,#d8d8d8)}
.member h4{position:absolute;left:25px;top:262px;font-size:18px;font-weight:600}
.member .role{position:absolute;left:25px;top:286px;font-size:11px;color:#555}
.member .socials{position:absolute;left:25px;top:334px;display:flex;gap:28px}
.social-dot{width:9px;height:9px;border-radius:50%;background:#333}

/* programs */
.programs{top:2392px;height:700px}
.program{top:183px;width:308px;height:392px;background:var(--white);box-shadow:0 2px 8px rgba(0,0,0,.08)}
.program-img{height:204px;position:relative}
.program-meta{position:absolute;left:20px;bottom:8px;color:var(--white);font-size:11px;font-weight:600}
.program h4{position:absolute;left:22px;top:228px;font-size:17px;font-weight:600}
.program p{position:absolute;left:22px;top:254px;width:240px;font-size:11px;line-height:22px;color:var(--text)}
.author{position:absolute;left:22px;top:336px;display:flex;align-items:center;gap:12px;font-size:11px;font-weight:600}
.avatar{width:36px;height:36px;border-radius:50%;background:linear-gradient(135deg,#ddd,#aaa)}
.tag{position:absolute;right:22px;top:346px;height:24px;padding:0 9px;color:var(--white);font-size:11px;display:flex;align-items:center}
.pager{top:618px;width:26px;height:26px;background:#ddd;display:flex;align-items:center;justify-content:center}

/* reviews */
.reviews{top:3117px;height:635px;background:var(--soft)}
.review{top:200px;width:308px;height:299px;background:var(--white);padding:54px 37px 0}
.review-head{display:flex;gap:14px;align-items:center}
.review-head .avatar{width:50px;height:50px}
.review-head strong{display:block;font-size:15px;font-weight:600}
.review-head span{font-size:11px;color:var(--text)}
.review p{margin-top:20px;font-size:12.5px;line-height:23px;color:var(--text)}
.stars{margin-top:8px;color:var(--pink-deep);font-size:13px;letter-spacing:2px}
.dot{top:530px;width:8px;height:8px;border-radius:50%;background:#ccc}

/* contact */
.contact{top:3752px;height:581px;background:var(--pink)}
.contact h2{left:92px;top:106px;font-size:26px;font-weight:600;color:var(--white)}
.contact .lead{left:92px;top:142px;font-size:13px;color:var(--white)}
.input{left:92px;width:474px;height:42px;background:var(--white);border:1px solid #ddd;font-size:11px;color:#999;padding:14px 10px 0}
.btn-send{left:92px;top:441px;width:150px;height:44px;border-radius:22px;background:var(--white);color:var(--ink);font-size:12px;display:flex;align-items:center;justify-content:center}
.contact-photo{left:600px;top:90px;width:487px;height:400px;font-size:11px;color:var(--dark);padding:6px 6px}

/* footer */
.site-footer{top:4333px;height:418px;background:var(--dark);color:#aaa}
.site-footer h5{position:absolute;font-size:16px;font-weight:600;color:var(--white)}
.ft{position:absolute;font-size:11px;line-height:22px;color:#aaa}
.ft-social{position:absolute;top:219px;display:flex;gap:28px}
.ft-social i{width:9px;height:9px;border-radius:2px;background:var(--blue)}
.ft-input{left:778px;top:156px;width:290px;height:31px;border-bottom:1px solid #444;font-size:11px;color:#aaa;padding:4px 10px 0}
.ft-btn{left:778px;top:206px;width:146px;height:43px;border:1px solid var(--white);border-radius:22px;color:var(--white);font-size:11px;display:flex;align-items:center;justify-content:center}
</style>
</head>
<body>

<header class="site-header">
  <div class="abs brand">PELDIVUX</div>
  <div class="abs nav-item active">Home</div>
  <div class="abs nav-item" style="left:355px">About</div>
  <div class="abs nav-item" style="left:427px">Our Team</div>
  <div class="abs nav-item" style="left:520px">General Information</div>
  <div class="abs nav-item" style="left:668px">Reviews</div>
  <div class="abs nav-item" style="left:753px">Contact</div>
  <div class="abs phone-dot"><svg width="12" height="12" viewBox="0 0 24 24"><path fill="#fff" d="M6.6 10.8a15.1 15.1 0 0 0 6.6 6.6l2.2-2.2c.3-.3.7-.4 1-.2 1.1.4 2.3.6 3.6.6.6 0 1 .4 1 1V20c0 .6-.4 1-1 1A17 17 0 0 1 3 4c0-.6.4-1 1-1h3.5c.6 0 1 .4 1 1 0 1.3.2 2.5.6 3.6.1.3 0 .7-.2 1z"/></svg></div>
  <div class="abs phone-num">+65 3090 4417</div>
  <div class="abs nav-item" style="left:1067px">Login</div>
</header>

<section class="hero" role="img" aria-label="Smiling woman sitting at a bright office desk beside a plant">
  <h1 class="abs">PELDIVUX manages communities throughout Southern Nevada</h1>
  <p class="abs">Accessible, licensed Association Managers 24 hour Web site access: online account information 24 hour emergency service</p>
  <div class="abs btn-outline">Discover more</div>
</section>

<section class="services">
  <div class="abs service-card" style="left:92px;height:320px">
    <div class="service-num">01</div>
    <h3>HOA MANAGEMENT</h3>
    <p>Lumaridge manages Community Associations, Business Parks, and Condo/Hotels throughout Northern and Southern Nevada, as well as in St.</p>
  </div>
  <div class="abs service-card" style="left:435px;height:340px">
    <div class="service-num">02</div>
    <h3>PROPERTY MANAGEMENT</h3>
    <p>Lumaridge partners with Homeowners across Southern and Northern Nevada to secure quality tenants and effectively manage Single Family homes. Experience excellence with us!</p>
  </div>
  <div class="abs service-card" style="left:778px;height:340px">
    <div class="service-num">03</div>
    <h3>REAL ESTATE SALES</h3>
    <p>We provide real value in a changing world with a range of services you can really feel at home with. Whether you are buying or selling, Lumaridge can help you get the deal you are looking for.</p>
  </div>
</section>

<section class="duties">
  <h2 class="abs">Collect all revenues and disburse payments to vendors as directed by the Board of Directors.</h2>
  <div class="abs duty" style="top:155px">
    <div class="abs duty-icon"><svg width="22" height="22" viewBox="0 0 24 24" fill="#fff"><circle cx="12" cy="8" r="3.5"/><circle cx="5" cy="10" r="2.5"/><circle cx="19" cy="10" r="2.5"/><path d="M5.5 20c0-3.6 2.9-6.5 6.5-6.5s6.5 2.9 6.5 6.5z"/></svg></div>
    <h4>24 hour emergency service</h4>
    <p>Lorem ipsum dolor sit amet, consectetur adipisicing elit. Sint ipsa voluptatibus.</p>
  </div>
  <div class="abs duty" style="top:251px">
    <div class="abs duty-icon"><svg width="22" height="22" viewBox="0 0 24 24" fill="#fff"><path d="M12 2l2.2 2.6 3.3-.7.7 3.3 3 1.6-1.4 3.2 1.4 3.2-3 1.6-.7 3.3-3.3-.7L12 22l-2.2-2.6-3.3.7-.7-3.3-3-1.6L4.2 12 2.8 8.8l3-1.6.7-3.3 3.3.7z"/></svg></div>
    <h4>Prepare the annual budget for.</h4>
    <p>Lorem ipsum dolor sit amet, consectetur adipisicing elit. Sint ipsa voluptatibus.</p>
  </div>
  <div class="abs duty" style="top:347px">
    <div class="abs duty-icon"><svg width="22" height="22" viewBox="0 0 24 24" fill="#fff"><path d="M3 3h18v18H3z" fill="none" stroke="#fff" stroke-width="2"/><rect x="6" y="12" width="2" height="6"/><rect x="10" y="8" width="2" height="10"/><rect x="14" y="10" width="2" height="8"/><rect x="18" y="6" width="1" height="12"/></svg></div>
    <h4>Prepare for and attend the budget.</h4>
    <p>Lorem ipsum dolor sit amet, consectetur adipisicing elit. Sint ipsa voluptatibus.</p>
  </div>

  <div class="abs signup">
    <h3>Signup today</h3>
    <div class="field" style="top:127px">Full name</div>
    <div class="field" style="top:175px">Your email address</div>
    <div class="field" style="top:224px">Your password</div>
    <div class="btn-white">Get started</div>
  </div>
</section>

<section class="team">
  <div class="section-title" style="top:92px">Our Team</div>
  <div class="section-sub" style="top:124px">Meet Professional Team Members</div>
  <div class="abs member" style="left:92px">
    <div class="member-photo" role="img" aria-label="Portrait of a bearded man in a hat and glasses"></div>
    <h4>Mark Wilson</h4><div class="role">24 hour emergency service</div>
    <div class="socials"><i class="social-dot"></i><i class="social-dot"></i><i class="social-dot"></i></div>
  </div>
  <div class="abs member" style="left:350px">
    <div class="member-photo" role="img" aria-label="Portrait of a red-haired woman in sunglasses"></div>
    <h4>Catherine</h4><div class="role">24 hour emergency service</div>
    <div class="socials"><i class="social-dot"></i><i class="social-dot"></i></div>
  </div>
  <div class="abs member" style="left:608px">
    <div class="member-photo" role="img" aria-label="Portrait of a woman in a striped shirt"></div>
    <h4>Jessie Ca</h4><div class="role">24 hour emergency service</div>
    <div class="socials"><i class="social-dot"></i><i class="social-dot"></i><i class="social-dot"></i></div>
  </div>
  <div class="abs member" style="left:864px">
    <div class="member-photo" role="img" aria-label="Portrait of a smiling man in sunglasses and denim shirt"></div>
    <h4>Andrew Berti</h4><div class="role">24 hour emergency service</div>
    <div class="socials"><i class="social-dot"></i><i class="social-dot"></i><i class="social-dot"></i></div>
  </div>
</section>

<section class="programs">
  <div class="section-title" style="top:92px">What do we do</div>
  <div class="section-sub" style="top:124px">Provide monthly financial reports to the Board of Directors</div>
  <div class="abs program" style="left:105px">
    <div class="program-img" role="img" aria-label="Students working together at a desk" style="background:linear-gradient(135deg,#c7cfd8,#8d97a3)"><div class="program-meta">20 / 7 / 2018 &nbsp; 4.5 Hours</div></div>
    <h4>PROPERTY MANAGEMENT</h4>
    <p>Lorem ipsum dolor sit amet, consectetur adipiscing elit.</p>
    <div class="author"><i class="avatar"></i>Jessica</div>
    <div class="tag" style="background:var(--blue)">USD 80</div>
  </div>
  <div class="abs program" style="left:439px">
    <div class="program-img" role="img" aria-label="Student writing in a bright library" style="background:linear-gradient(135deg,#dfe4e8,#9aa5ae)"><div class="program-meta">15 / 8 / 2018 &nbsp; 6 Hours</div></div>
    <h4>REAL ESTATE SALES</h4>
    <p>Lorem ipsum dolor sit amet, consectetur adipiscing elit.</p>
    <div class="author"><i class="avatar"></i>Catherine</div>
    <div class="tag" style="background:var(--pink)">Free</div>
  </div>
  <div class="abs program" style="left:774px">
    <div class="program-img" role="img" aria-label="Children drawing in a classroom" style="background:linear-gradient(135deg,#e9c8a8,#a88f7a)"><div class="program-meta">10 / 8 / 2018 &nbsp; 8 Hours</div></div>
    <h4>Summer Kids</h4>
    <p>Lorem ipsum dolor sit amet, consectetur adipiscing elit.</p>
    <div class="author"><i class="avatar"></i>Mark Wilson</div>
    <div class="tag" style="background:var(--blue)">USD 45</div>
  </div>
  <div class="abs pager" style="left:562px"><svg width="8" height="8" viewBox="0 0 8 8"><path d="M5.5 1L2.5 4l3 3" stroke="#fff" fill="none"/></svg></div>
  <div class="abs pager" style="left:597px"><svg width="8" height="8" viewBox="0 0 8 8"><path d="M2.5 1l3 3-3 3" stroke="#fff" fill="none"/></svg></div>
</section>

<section class="reviews">
  <div class="section-title" style="top:92px">Student Reviews</div>
  <div class="section-sub" style="top:124px">from around the world</div>
  <div class="abs review" style="left:105px">
    <div class="review-head"><i class="avatar"></i><div><strong>Andrio</strong><span>Web Developer</span></div></div>
    <p>Nam eget mi eu ante faucibus viverra nec sed magna. Vivamus viverra sapien ex, elementum varius ex sagittis vel.</p>
    <div class="stars">★★★★</div>
  </div>
  <div class="abs review" style="left:439px">
    <div class="review-head"><i class="avatar"></i><div><strong>Jackson</strong><span>Cartwell Developer</span></div></div>
    <p>You really do help young creative minds to get quality education and professional job search assistance. I'd recommend it to everyone!</p>
    <div class="stars">★★★★</div>
  </div>
  <div class="abs review" style="left:774px">
    <div class="review-head"><i class="avatar"></i><div><strong>Camila</strong><span>Marketing Manager</span></div></div>
    <p>Trying something new is exciting! Thanks for the amazing law course and the great teacher who was able to make it interesting.</p>
    <div class="stars">★★★</div>
  </div>
  <i class="abs dot" style="left:578px"></i>
  <i class="abs dot" style="left:600px;background:#888"></i>
</section>

<section class="contact">
  <h2 class="abs">Contact us</h2>
  <div class="abs lead">we love conversations. let us talk!</div>
  <div class="abs input" style="top:188px">Enter full name</div>
  <div class="abs input" style="top:242px">Enter email address</div>
  <div class="abs input" style="top:293px;height:130px;padding-top:8px">Tell us about your message</div>
  <div class="abs btn-send">Send Message</div>
  <div class="abs contact-photo" role="img" aria-label="Two smiling girls">Smiling Two Girls</div>
</section>

<footer class="site-footer">
  <h5 style="left:92px;top:110px">Headquarter</h5>
  <div class="ft" style="left:92px;top:138px">1800 dapibus a tortor pretium,<br>Integer nisl dui, ABC 12000</div>
  <div class="ft-social" style="left:102px"><i></i><i></i><i></i></div>
  <div class="ft" style="left:92px;top:247px">Copyright © 2019 PELDIVUX</div>

  <h5 style="left:435px;top:110px">Contact Info</h5>
  <div class="ft" style="left:435px;top:138px">+65 3090 4417, +66 3090 5528<br>hello@peldivux.example</div>
  <h5 style="left:435px;top:222px">Quick Links</h5>
  <div class="ft" style="left:435px;top:252px">Career &nbsp;&nbsp; Investor &nbsp;&nbsp; Terms &amp; Conditions<br>Refund Policy</div>

  <h5 style="left:778px;top:110px">Newsletter Signup</h5>
  <div class="abs ft-input">Enter your email</div>
  <div class="abs ft-btn">Send me</div>
  <div class="ft" style="left:778px;top:264px;font-size:9px">* Please note - we do not spam your email.</div>
</footer>

</body>
</html>
```